Child Care Centre needs new roadside billboard / sign*

We have a 2400mm x 1200mm sign that needs to be refreshed. The design is dated and we want to create a new cleaner, more readable roadside signIt needs to be readable from about 100m awayThe text requirements are simple, but we need it to have a warm, family feel.We are located in a small beach side community and we have a lot of bright colours in our centre (a lot of blues and yellows)https://www.maplegrovechildcare.com.au/

Target Market(s)

Parents of young children

Industry/Entity Type

Childcare

Colors
fbed22
0355a3

Requirements
Must have
• Readable from c.100m
• Simple, warm design
Should not have
• Cluttered or overly busy

```html
<!DOCTYPE html>
<html lang="en">
<head>
<meta charset="utf-8">
<title>Maple Grove Early Education – Roadside Sign</title>
<link rel="stylesheet" href="https://fonts.googleapis.com/css2?family=Montserrat:wght@800&family=Open+Sans:wght@600&display=swap">
<style>
  :root {
    --page-bg: #e6e6e6;
    --sun-yellow: #fcd605;
    --ocean-blue: #0366b4;
    --cyan: #4fcfee;
    --sky-light: #dff1fb;
    --sky-mid: #b9e2f4;
    --mascot-yellow: #f6e92e;
    --magenta: #e6008a;
    --ink: #111111;
    --white: #ffffff;
    --band-purple: #a79fc9;
    --band-blue: #86c2f0;
    --band-green: #9fce98;
    --band-peach: #f5d6a0;
    --band-salmon: #f9b99a;
    --band-pink: #f4a3a8;
  }
  * { margin: 0; padding: 0; box-sizing: border-box; }
  html, body {
    width: 1200px; height: 1200px; overflow: hidden;
    background: var(--page-bg);
  }
  .sign {
    position: absolute; left: 40px; top: 320px;
    width: 1120px; height: 560px; display: block;
  }
  .brand-name {
    font-family: "Montserrat", sans-serif; font-weight: 800;
    fill: var(--ink);
  }
  .offer-text {
    font-family: "Open Sans", sans-serif; font-weight: 600;
    fill: var(--white);
  }
  .services-text, .phone-number {
    font-family: "Montserrat", sans-serif; font-weight: 800;
    fill: var(--ink);
  }
</style>
</head>
<body>
<svg class="sign" viewBox="0 0 1800 900" xmlns="http://www.w3.org/2000/svg" aria-label="Maple Grove Early Education roadside sign">
  <defs>
    <linearGradient id="sky-fade" x1="0" y1="0" x2="0" y2="1">
      <stop offset="0" stop-color="var(--sky-light)"/>
      <stop offset="1" stop-color="var(--sky-mid)"/>
    </linearGradient>
    <clipPath id="sky-clip">
      <path d="M150,0 L1800,0 L1800,450 C1500,650 1100,760 800,740 C450,720 200,500 140,250 C130,150 140,60 150,0 Z"/>
    </clipPath>
  </defs>

  <!-- background -->
  <rect class="sign-base" width="1800" height="900" fill="var(--sun-yellow)"/>

  <!-- left side stripes -->
  <path class="stripe-light" d="M135,0 L175,0 C120,300 180,650 410,900 L230,900 C100,650 90,300 135,0 Z" fill="#eef4f6"/>
  <path class="stripe-cyan" d="M95,0 L125,0 C75,300 95,650 230,900 L195,900 C65,650 45,300 95,0 Z" fill="var(--cyan)"/>
  <path class="stripe-blue" d="M0,0 L75,0 C25,300 35,650 120,900 L0,900 Z" fill="var(--ocean-blue)"/>

  <!-- sky with rainbow bands -->
  <g class="sky" clip-path="url(#sky-clip)">
    <rect width="1800" height="900" fill="url(#sky-fade)"/>
    <g class="rainbow" fill="none" stroke-width="46">
      <circle cx="1300" cy="1700" r="1727" stroke="var(--band-purple)"/>
      <circle cx="1300" cy="1700" r="1681" stroke="var(--band-blue)"/>
      <circle cx="1300" cy="1700" r="1635" stroke="var(--band-green)"/>
      <circle cx="1300" cy="1700" r="1589" stroke="var(--band-peach)"/>
      <circle cx="1300" cy="1700" r="1543" stroke="var(--band-salmon)"/>
      <circle cx="1300" cy="1700" r="1497" stroke="var(--band-pink)"/>
    </g>
  </g>

  <!-- brand -->
  <circle class="brand-mark" cx="360" cy="270" r="95" fill="var(--mascot-yellow)"/>
  <text class="brand-name" x="510" y="235" font-size="128">Maple Grove</text>
  <text class="brand-name" x="590" y="370" font-size="96">Early Education</text>

  <!-- offer panel -->
  <rect class="offer-panel" x="287" y="488" width="1228" height="190" rx="14" fill="var(--magenta)" stroke="var(--ink)" stroke-width="4"/>
  <text class="offer-text" x="900" y="555" font-size="62" text-anchor="middle">6 weeks to 6 years (LONG DAY CARE)</text>
  <line class="offer-divider" x1="640" y1="585" x2="1162" y2="585" stroke="var(--white)" stroke-width="3"/>
  <text class="offer-text" x="900" y="652" font-size="60" text-anchor="middle">Open 6.30 am – 6.30 pm | 52 weeks a year</text>

  <!-- services and phone -->
  <text class="services-text" x="900" y="757" font-size="50" text-anchor="middle">Before and After School Care | Vacation Care</text>
  <text class="phone-number" x="900" y="845" font-size="92" text-anchor="middle">07 4000 2618</text>
</svg>
</body>
</html>
```